Webdesign für vielseitiges Unternehmen
Zielgruppe
Die Seite wird HOCHMOOR-ART oder DESIGN heißen.
Das Unternehmen bietet folgende Segmente an:
1. Möbelstücke (meist Unikate, da restauriert mit eigener Kreation)
2. Fotografien
3. Malerei
4. Interieurdesign (Gestalten, Einrichten von Apartments, Häusern, Shops etc.) (hier muss natürlich mehr Platz für Informationstext sein.
5. Gallery. - Infos zu Öffnungszeiten und Bilder ebenfalls.
6. Die Location ist für Events buchbar
(7.) Blogg wenns nicht zu aufwändig ist. (hier möchte ich gern Bilder posten die ich irgendwo finde und als gut erachte. Oder Produkte. Wichtig ist, dass bei Verbreitung von Fremdpostings, immer die Quelle eingefügt werden muss. Am besten automatisch. Ich muss zu dem Post noch eigenes Kommentar abgeben können.
Für jedes Segment soll eine Unterseite geschaffen werden.
Die Produktfotos sollen clean aufgebaut sein. Am besten je Produkt 1 Bild pro Seite. Vielleicht erst nachdem man auf ein Bild in der Auswahl geklickt hat?? 3 nebeneinander und dann neue Zeile.
Unter den Bildern (hauptsächlich Querformat aber Hochformat muss auch gehen) müssen Angaben stehen:
-Art
-Size
-Auflage
-Preis
-liken für Social Media oder weiterleiten (wenn möglich)
-Fragen zu diesem Produkt ( wenn hier jemand klickt und etwas schreibt, muss ich eine mail erhalten, wo ich direkt ersehen kann, zu welchem Produkt die Frage zugeordnet ist.
Pro Artikel müssen mehrere Bilder eingestellt werden können, die der Client durch einfaches klicken durchklicken kann.
Die Seite soll clean, chic und Edel wirken. Hauptsächlich über Bilder. Shopsystem ist wegen Aufwandskosten erstmal nicht geplant)
Ich muss die Seite selber pflegen können, auch SEO Optimieren (ohne Programierkenntnisse)
Die Seite soll eine Seite für verschiedene Aspekte sein wie:
- Gallerie
hier wird die Gallerie vorgestellt und Bilder gezeigt von Ausstellungen und Künstlervorstellung..
Aufgabenstellung
Schwarz- Weiß
Akzente eventuell in Patinagrün oder Grünspan oder Malachitgrün oder Gold
Mobilgeräte responsiv

```html
<!DOCTYPE html>
<html lang="de">
<head>
<meta charset="utf-8">
<title>HOCHMOOR-ART – Interieur · Design · Galerie</title>
<link rel="stylesheet" href="https://fonts.googleapis.com/css2?family=Figtree:wght@400;500;600;700&display=swap">
<style>
:root{
  --page:#f6f6f6;
  --white:#ffffff;
  --ink:#1d1d1f;
  --text:#2b2b2b;
  --muted:#7d7d7d;
  --night:#1b1a1c;
  --bronze:#4b4232;
  --patina:#4a7463;
  --patina-soft:#6e8f72;
  --sage:#d4ddd4;
  --gold:#f7dc83;
  --gold-deep:#d6c679;
  --gold-line:#f3d66c;
  --field-line:#f0dc98;
}
*{box-sizing:border-box;margin:0;padding:0}
html,body{width:1200px;height:2886px;overflow:hidden}
body{background:var(--page);font-family:"Figtree",sans-serif;color:var(--text);position:relative}

.brand{position:absolute;top:60px;left:0;width:1200px;text-align:center}
.brand-name{font-size:54px;font-weight:600;letter-spacing:6px;color:var(--ink);line-height:1}
.brand-tagline{margin-top:16px;font-size:13.5px;letter-spacing:4.2px;color:var(--ink);font-weight:500}

.feature{position:absolute;left:100px;width:1001px;height:386px;border-radius:12px;overflow:hidden}
.feature-photo{position:absolute;top:0;height:100%}
.feature-copy{position:absolute;top:0;width:345px}
.feature-title{font-size:41px;font-weight:400;line-height:1;letter-spacing:.3px}
.feature-text{margin-top:28px;font-size:13.4px;line-height:21px}
.feature-button{position:absolute;width:141px;height:46px;border-radius:4px;font-size:17.5px;display:flex;align-items:center;justify-content:center}
.dots{position:absolute;display:flex;gap:11px;align-items:center}
.dot{width:6px;height:6px;border-radius:50%;background:rgba(255,255,255,.55)}
.dot.active{width:14px;height:14px;border:1.5px solid #fff;background:transparent;display:flex;align-items:center;justify-content:center}
.dot.active::after{content:"";width:6px;height:6px;border-radius:50%;background:#fff}
.arrow{position:absolute;width:52px;height:52px}

.gallery{top:202px;background:var(--night)}
.gallery .feature-photo{left:0;width:482px;background:linear-gradient(90deg,#2a2a2c 0%,#cfcfd1 14%,#ececee 45%,#dcdcde 80%,#8d8d90 96%,#1b1a1c 100%)}
.gallery .feature-copy{left:511px;top:72px;width:380px;color:#fff}
.gallery .feature-text{color:#e8e8e8}
.gallery .feature-button{left:511px;top:242px;background:var(--bronze);color:#fff}
.gallery .dots{left:511px;top:333px}

.photo{top:608px;background:var(--white)}
.photo .feature-photo{left:471px;width:530px;background:linear-gradient(160deg,#c9cfc4 0%,#d7c49a 40%,#c9a66a 65%,#e6e1d6 100%)}
.photo .feature-copy{left:85px;top:84px;color:var(--ink)}
.photo .feature-button{left:85px;top:274px;background:var(--sage);color:var(--ink)}

.painting{top:1016px;background:var(--patina)}
.painting .feature-photo{left:0;width:478px;background:linear-gradient(120deg,#8e8a80 0%,#a89c86 35%,#b48a62 55%,#7c837c 80%,#5d6a5e 100%)}
.painting .feature-copy{left:511px;top:78px;color:#fff}
.painting .feature-text{color:#eef3ef}
.painting .feature-button{left:511px;top:254px;background:var(--patina-soft);color:#fff}
.painting .dots{left:511px;top:334px}

.interior{top:1424px;background:var(--gold)}
.interior .feature-photo{left:490px;width:511px;background:linear-gradient(90deg,var(--gold) 0%,#d9d6cc 14%,#e4e2dc 45%,#c8c7c3 60%,#e4e2dc 78%,#f0e6b8 94%,var(--gold) 100%)}
.interior .feature-copy{left:85px;top:90px;color:var(--ink)}
.interior .feature-button{left:85px;top:292px;background:var(--gold-deep);color:var(--ink)}

.contact-title{position:absolute;top:1868px;left:0;width:1200px;text-align:center;font-size:42px;font-weight:400;color:var(--patina);letter-spacing:.5px}
.contact-rule{position:absolute;top:1916px;left:538px;width:112px;height:5px;border-radius:3px;background:var(--gold-line)}
.field{position:absolute;left:267px;width:666px;height:60px;border:1.5px solid var(--field-line);background:var(--page);padding:18px 19px;font-size:17.5px;color:#7c8a94}
.field.message{height:161px}
.submit{position:absolute;left:536px;top:2466px;width:128px;height:40px;background:var(--patina);color:#fff;font-size:16.5px;font-weight:600;display:flex;align-items:center;justify-content:center}

.site-footer{position:absolute;top:2558px;left:0;width:1200px;height:246px;background:var(--white)}
.footer-col{position:absolute;top:48px}
.footer-heading{font-size:20px;font-weight:400;color:var(--ink);margin-bottom:18px}
.footer-link{font-size:14px;color:var(--muted);line-height:31.5px}
.newsletter-text{font-size:13.5px;color:var(--muted);line-height:16.5px;width:280px;margin-top:-4px}
.newsletter-form{position:absolute;top:100px;left:0;width:234px;height:38px;border:1.5px solid var(--patina);border-radius:5px;background:#fff;overflow:hidden}
.newsletter-placeholder{position:absolute;left:14px;top:10px;font-size:12px;color:#b6b6b6}
.newsletter-send{position:absolute;right:0;top:0;width:58px;height:100%;background:var(--patina);display:flex;align-items:center;justify-content:center}

.legal-bar{position:absolute;top:2804px;left:0;width:1200px;height:82px;background:var(--page)}
.social{position:absolute;top:28px;width:14px;height:14px;border-radius:50%;background:var(--ink)}
</style>
</head>
<body>

<header class="brand">
  <div class="brand-name">HOCHMOOR-ART</div>
  <div class="brand-tagline">INTERIEUR · DESIGN · GALERIE</div>
</header>

<section class="feature gallery">
  <div class="feature-photo" role="img" aria-label="Heller Galerieraum mit gerahmten Bildern und schwarzer Bogenskulptur"></div>
  <svg class="arrow" style="left:14px;top:167px" viewBox="0 0 52 52"><circle cx="26" cy="26" r="26" fill="rgba(0,0,0,.12)"/><path d="M30 16 L20 26 L30 36" fill="none" stroke="#fff" stroke-width="1.6"/></svg>
  <div class="feature-copy">
    <h2 class="feature-title">Gallerie</h2>
    <p class="feature-text">hier wird die Gallerie vorgestellt und Bilder gezeigt<br>von Ausstellungen und Künstler-vorstellungen</p>
  </div>
  <div class="feature-button">Frage stellen</div>
  <div class="dots"><span class="dot active"></span><span class="dot"></span><span class="dot"></span><span class="dot"></span></div>
  <svg class="arrow" style="left:934px;top:167px" viewBox="0 0 52 52"><circle cx="26" cy="26" r="26" fill="rgba(255,255,255,.07)"/><path d="M22 16 L32 26 L22 36" fill="none" stroke="#fff" stroke-width="1.6"/></svg>
</section>

<section class="feature photo">
  <div class="feature-photo" role="img" aria-label="Hand hält ein Kameraobjektiv vor herbstlicher Landschaft"></div>
  <svg class="arrow" style="left:4px;top:167px" viewBox="0 0 52 52"><path d="M30 16 L20 26 L30 36" fill="none" stroke="#c8c8c8" stroke-width="1.6"/></svg>
  <div class="feature-copy">
    <h2 class="feature-title">Fotografie</h2>
    <p class="feature-text">hier werden Fotografien als Produkte gezeigt mit den Untertexten wie Art, Größe, Preis und die Möglichkeit, sich mehrere Bilder dazu nzuschauen. und zu diesem Artikel Fragen zu stellen.</p>
  </div>
  <div class="feature-button">Frage stellen</div>
  <svg class="arrow" style="left:944px;top:167px" viewBox="0 0 52 52"><path d="M22 16 L32 26 L22 36" fill="none" stroke="#e8e8e8" stroke-width="1.6"/></svg>
</section>

<section class="feature painting">
  <div class="feature-photo" role="img" aria-label="Maler im Atelier vor einer Steinwand mit farbigen Bildern"></div>
  <svg class="arrow" style="left:14px;top:167px" viewBox="0 0 52 52"><circle cx="26" cy="26" r="26" fill="rgba(0,0,0,.1)"/><path d="M30 16 L20 26 L30 36" fill="none" stroke="#fff" stroke-width="1.6"/></svg>
  <div class="feature-copy">
    <h2 class="feature-title">Malerei</h2>
    <p class="feature-text">hier werden Bilder als Produkte gezeigt mit den Untertexten wie Art, Größe, Preis und die Möglichkeit, sich mehrere Bilder dazu anzuschauen. und zu diesem Artikel eine Frage zu stellen.</p>
  </div>
  <div class="feature-button">Frage stellen</div>
  <div class="dots"><span class="dot active"></span><span class="dot"></span><span class="dot"></span><span class="dot"></span></div>
  <svg class="arrow" style="left:934px;top:167px" viewBox="0 0 52 52"><circle cx="26" cy="26" r="26" fill="rgba(255,255,255,.07)"/><path d="M22 16 L32 26 L22 36" fill="none" stroke="#fff" stroke-width="1.6"/></svg>
</section>

<section class="feature interior">
  <div class="feature-photo" role="img" aria-label="Dunkler Polstersessel in einem hellen Raum am Fenster"></div>
  <svg class="arrow" style="left:4px;top:167px" viewBox="0 0 52 52"><path d="M30 16 L20 26 L30 36" fill="none" stroke="#f0e4b4" stroke-width="1.6"/></svg>
  <div class="feature-copy">
    <h2 class="feature-title">Interieur</h2>
    <p class="feature-text">hier werden Produkte wie Möbel gezeigt mit den Untertexten wie Art, Größe, Preis und die Möglichkeit, sich mehrere Bilder dazu anzuschauen. und zu diesem Artikel eine Frage zu stellen.</p>
  </div>
  <div class="feature-button">Frage stellen</div>
  <svg class="arrow" style="left:944px;top:167px" viewBox="0 0 52 52"><path d="M22 16 L32 26 L22 36" fill="none" stroke="#f3e3a4" stroke-width="1.6"/></svg>
</section>

<h2 class="contact-title">Kontakt</h2>
<div class="contact-rule"></div>
<div class="field" style="top:1989px">Name</div>
<div class="field" style="top:2082px">Email</div>
<div class="field" style="top:2176px">Anliegen</div>
<div class="field message" style="top:2270px">Nachricht</div>
<div class="submit">Absenden</div>

<footer class="site-footer">
  <div class="footer-col" style="left:100px">
    <h3 class="footer-heading">Links</h3>
    <div class="footer-link">Home</div><div class="footer-link">Shop</div><div class="footer-link">Blog</div><div class="footer-link">Contact</div>
  </div>
  <div class="footer-col" style="left:355px">
    <h3 class="footer-heading">Mehr infos</h3>
    <div class="footer-link">Über Uns</div><div class="footer-link">Team</div><div class="footer-link">Jobs</div><div class="footer-link">Impressum</div>
  </div>
  <div class="footer-col" style="left:611px">
    <h3 class="footer-heading">Support</h3>
    <div class="footer-link">FAQ</div><div class="footer-link">AGBs</div><div class="footer-link">Datenschutz</div>
  </div>
  <div class="footer-col" style="left:866px;width:334px;height:150px">
    <h3 class="footer-heading">Newsletter</h3>
    <p class="newsletter-text">Melden Sie sich jetzt für unseren Newsletter an und verpassen Sie keine Neuigkeiten.</p>
    <div class="newsletter-form">
      <span class="newsletter-placeholder">Emailadresse</span>
      <span class="newsletter-send"><svg width="22" height="20" viewBox="0 0 22 20"><path d="M2 2 L20 10 L2 18 L5 10 Z M5 10 H20" fill="none" stroke="#fff" stroke-width="1.6" stroke-linejoin="round"/></svg></span>
    </div>
  </div>
</footer>

<div class="legal-bar">
  <span class="social" style="left:998px" aria-label="Social-Media-Profil"></span>
  <span class="social" style="left:1041px" aria-label="Social-Media-Profil"></span>
  <span class="social" style="left:1083px" aria-label="Social-Media-Profil"></span>
</div>

</body>
</html>
```